Take my logo and make me some cool looking business cards

I've got a logo that we've trademarked so you can't change the logo but you can change it's color combo and find a fun way to incorporate it into a new business card design that is fresh, stylish, and can be applied to some cool medium cost materials (plastic, wood, metal, etc). Basically, we're looking for business cards that stand out in a good way.
Here's the logo we're currently using:
Thanks to everyone that has submitted designs. We've narrowed down to the top 4 designs and tried to eliminate old versions or designs that just didn't match our vision as quickly as we could. We don't plan on keeping this open for the full 9 days; we plan on selecting a design in the next 48 hours; with the goal of having something in the hands of a printer, preferably plastic printer, by Thursday AM Pacific Time.
Business
- must include our existing logo

```html
<!DOCTYPE html>
<html lang="en">
<head>
<meta charset="utf-8">
<title>Skylark Business Card</title>
<link rel="stylesheet" href="https://fonts.googleapis.com/css2?family=Cinzel:wght@400;600&display=swap">
<style>
  :root {
    --backdrop: #3b3b3d;
    --brand-blue: #0f5aa8;
    --brand-blue-light: #3f86cf;
    --card-white: #ffffff;
    --ink: #4a4f57;
    --shadow: rgba(0, 0, 0, 0.45);
  }
  * { margin: 0; padding: 0; box-sizing: border-box; }
  html, body {
    width: 1200px;
    height: 900px;
    overflow: hidden;
    background: var(--backdrop);
    font-family: "Cinzel", Georgia, serif;
  }
  .canvas {
    position: relative;
    width: 1200px;
    height: 900px;
  }
  .card {
    position: absolute;
    left: 290px;
    width: 620px;
    height: 354px;
    overflow: hidden;
    box-shadow: 0 12px 30px var(--shadow);
  }
  .card--front { top: 72px; background: var(--card-white); }
  .card--back  { top: 470px; background: var(--brand-blue); }

  .wordmark {
    position: absolute;
    font-weight: 600;
    letter-spacing: 1px;
    line-height: 1;
  }
  .card--front .wordmark {
    left: 36px;
    top: 38px;
    font-size: 36px;
    color: var(--brand-blue);
  }
  .card--back .wordmark {
    left: 0;
    right: 0;
    top: 156px;
    text-align: center;
    font-size: 42px;
    color: var(--card-white);
  }

  .name-band {
    position: absolute;
    left: 0;
    top: 120px;
    width: 258px;
    height: 32px;
    background: var(--brand-blue);
  }
  .name-band .icon-box {
    position: absolute;
    left: 34px;
    top: 3px;
    width: 26px;
    height: 26px;
    background: var(--brand-blue-light);
  }
  .name-band .person-name {
    position: absolute;
    left: 78px;
    top: 6px;
    font-size: 18px;
    color: var(--card-white);
    letter-spacing: 0.5px;
    white-space: nowrap;
  }
  .job-title {
    position: absolute;
    left: 0;
    width: 252px;
    top: 160px;
    text-align: right;
    font-size: 14px;
    letter-spacing: 7px;
    color: var(--brand-blue);
  }

  .contact-list {
    position: absolute;
    right: 146px;
    top: 0;
    text-align: right;
    font-size: 10.5px;
    color: var(--ink);
    letter-spacing: 0.3px;
    line-height: 1.45;
  }
  .contact-list .address { position: absolute; right: 0; top: 110px; white-space: nowrap; }
  .contact-list .phone   { position: absolute; right: 0; top: 180px; white-space: nowrap; }
  .contact-list .email   { position: absolute; right: 0; top: 238px; white-space: nowrap; }

  .contact-stripe {
    position: absolute;
    left: 486px;
    top: 0;
    width: 26px;
    height: 100%;
    background: var(--brand-blue);
  }
  .contact-stripe .icon-box {
    position: absolute;
    left: 2px;
    width: 22px;
    height: 22px;
    background: var(--brand-blue-light);
  }
  .contact-stripe .icon-home  { top: 110px; }
  .contact-stripe .icon-phone { top: 174px; }
  .contact-stripe .icon-mail  { top: 232px; }
  .icon-box svg { display: block; width: 100%; height: 100%; }
</style>
</head>
<body>
<main class="canvas">

  <section class="card card--front" aria-label="Business card front">
    <div class="wordmark">SKYLARK</div>

    <div class="name-band">
      <span class="icon-box">
        <svg viewBox="0 0 26 26" aria-hidden="true">
          <circle cx="13" cy="10" r="5" fill="#ffffff"/>
          <path d="M4 24c0-6 4-9 9-9s9 3 9 9z" fill="#ffffff"/>
        </svg>
      </span>
      <span class="person-name">DANA WHITMORE</span>
    </div>
    <div class="job-title">CEO</div>

    <div class="contact-list">
      <p class="address">418 HARBOR LANE<br>SEACLIFF BAY, CA 90210</p>
      <p class="phone">+15550142378</p>
      <p class="email">DW@SKYLARK.COM</p>
    </div>

    <div class="contact-stripe">
      <span class="icon-box icon-home">
        <svg viewBox="0 0 22 22" aria-hidden="true">
          <path d="M11 4 3 11h2.5v7h4.5v-5h2v5h4.5v-7H19z" fill="#ffffff"/>
        </svg>
      </span>
      <span class="icon-box icon-phone">
        <svg viewBox="0 0 22 22" aria-hidden="true">
          <path d="M4 9c0-3 3-5 7-5s7 2 7 5h-3.5V7.5h-7V9z" fill="#ffffff"/>
          <rect x="5" y="10" width="12" height="8" rx="1.5" fill="#ffffff"/>
          <circle cx="11" cy="14" r="2.2" fill="#3f86cf"/>
        </svg>
      </span>
      <span class="icon-box icon-mail">
        <svg viewBox="0 0 22 22" aria-hidden="true">
          <rect x="4" y="6" width="14" height="10" fill="#ffffff"/>
          <path d="M4 6l7 6 7-6" fill="none" stroke="#3f86cf" stroke-width="1.3"/>
        </svg>
      </span>
    </div>
  </section>

  <section class="card card--back" aria-label="Business card back">
    <div class="wordmark">SKYLARK</div>
  </section>

</main>
</body>
</html>
```